Company Website Re-design for Software development consultancy

We would like our company website to be redesigned using our existing marketing collateral and website content as a guide

current site : www.brackenloft.com.au

For the different pages types and content please base on the following site : https://www.quorvanta.net/

We want a coded site - but will replace the content ourselves within the sections you provide to customise to our needs.

Target Market(s)

Medium to Large corporates needing software design and development services

Industry/Entity Type

Information Technology

Coding

Coded - Design and coding required

Number of Pages Required

5+ page

Font styles to use
Sans Serif

Colors
ec1f27
ffffff
000000

Requirements
Must have
• Align to colour scheme of existing collateral
• Include pages for the key areas of our busines - see : https://www.quorvanta.net/
Nice to have
• image rotators - make the site interesting to the business visitor

```html
<!DOCTYPE html>
<html lang="en">
<head>
<meta charset="utf-8">
<title>Bracken Loft — Software Development Consultancy</title>
<link rel="stylesheet" href="https://fonts.googleapis.com/css2?family=Montserrat:wght@700;800&family=Open+Sans:wght@400;600;700&display=swap">
<style>
:root{
  --red:#ec1f27;
  --red-deep:#c8151c;
  --white:#ffffff;
  --black:#000000;
  --ink:#1d1d1d;
  --body:#555555;
  --line:#bdbdbd;
  --grey-band:#efefef;
  --head:'Montserrat',sans-serif;
  --text:'Open Sans',sans-serif;
}
*{box-sizing:border-box;margin:0;padding:0}
html,body{width:1200px;height:3261px;overflow:hidden;background:var(--white)}
body{font-family:var(--text);color:var(--body)}
.page{position:relative;width:1200px;height:3261px;overflow:hidden}
.abs{position:absolute}
.center{left:0;width:1200px;text-align:center}

/* hero */
.hero{position:absolute;left:0;top:0;width:1200px;height:620px;
  background:linear-gradient(180deg,#3f6c9a 0%,#7d8fa4 30%,#d9a24e 55%,#e0a13c 62%,#2c3a4d 72%,#4a6e8e 85%,#6d8da8 100%)}
.brand{position:absolute;left:98px;top:30px;display:flex;align-items:center;gap:12px;color:var(--white);
  font-family:var(--text);font-weight:700;font-size:30px;letter-spacing:0.5px}
.brand-dot{width:64px;height:64px;border:4px solid var(--white);border-radius:50%}
.menu-toggle{position:absolute;left:1060px;top:50px}
.hero-title{top:165px;font-family:var(--text);font-weight:700;font-size:98px;color:var(--white);letter-spacing:2px;line-height:1.1;text-shadow:0 2px 8px rgba(0,0,0,.25)}
.hero-sub{top:290px;font-size:28px;color:#f0f0f0}
.btn-quote{position:absolute;left:502px;top:359px;width:196px;height:64px;border-radius:32px;background:var(--red);
  color:var(--white);font-weight:700;font-size:18px;line-height:64px;text-align:center}

/* section headings */
.section-title{font-family:var(--head);font-weight:800;font-size:44px;color:var(--ink);letter-spacing:0.5px;line-height:1}
.section-sub{font-size:26px;color:#444}

/* services */
.service{position:absolute;top:852px;width:317px;height:292px;border:1.5px solid var(--line);text-align:center}
.service svg{position:absolute;left:50%;transform:translateX(-50%);top:26px}
.service h3{position:absolute;top:118px;width:100%;font-family:var(--text);font-weight:600;font-size:26px;color:var(--ink)}
.service p{position:absolute;top:170px;left:18px;right:18px;font-size:15px;line-height:25px;color:#666}

/* what we do */
.band-grey{position:absolute;left:0;top:1235px;width:1200px;height:548px;background:var(--grey-band)}
.wwd-frame{position:absolute;left:98px;top:1311px;width:596px;height:398px;border:1.5px solid #9a9a9a}
.wwd-title{position:absolute;left:154px;top:1355px;font-family:var(--head);font-weight:800;font-size:42px;color:var(--ink)}
.wwd-copy{position:absolute;left:154px;top:1420px;width:440px;font-size:14px;line-height:26px;color:#666}
.wwd-copy p+p{margin-top:26px}
.btn-outline{position:absolute;left:154px;top:1604px;width:144px;height:53px;border:2px solid var(--red);border-radius:27px;
  color:var(--red);font-weight:700;font-size:15px;line-height:49px;text-align:center}
.video{position:absolute;left:633px;top:1341px;width:467px;height:337px;
  background:linear-gradient(135deg,#b9b3ab 0%,#8c8f94 40%,#3d4a58 100%);box-shadow:0 6px 18px rgba(0,0,0,.3)}
.play{position:absolute;left:833px;top:1476px}

/* team */
.team-intro{top:1928px;font-size:15px;line-height:28px;color:#444}
.member{position:absolute;top:2019px;width:300px;text-align:center}
.avatar{margin:0 auto;width:248px;height:248px;border-radius:50%;border:2px solid #cfcfcf;padding:6px}
.avatar span{display:block;width:100%;height:100%;border-radius:50%;background:linear-gradient(180deg,#d9dcdb 0%,#a8aaa9 55%,#2c2f33 100%)}
.member h4{margin-top:25px;font-family:var(--text);font-weight:600;font-size:26px;color:var(--ink)}
.member .role{margin-top:6px;font-size:15px;color:var(--red);letter-spacing:.5px}
.member p{margin:10px auto 0;width:250px;font-size:15px;line-height:26px;color:#666}

/* contact */
.contact{position:absolute;left:0;top:2500px;width:1200px;height:452px;
  background:linear-gradient(120deg,#d8121b 0%,#e83a40 40%,#c8151c 70%,#e5474c 100%)}
.contact-title{top:2556px;font-family:var(--head);font-weight:800;font-size:44px;color:var(--white)}
.field{position:absolute;background:var(--white);font-size:14px;color:#777;padding:10px 14px}
.btn-submit{position:absolute;left:537px;top:2854px;width:126px;height:50px;border:2px solid var(--white);border-radius:25px;
  color:var(--white);font-weight:700;font-size:16px;line-height:46px;text-align:center}

/* footer */
.social{position:absolute;top:3030px;width:50px;height:50px;border:1.5px solid #999;border-radius:50%}
.foot-line{font-size:15px;color:#444}
.foot-line .sep{margin:0 10px}
.foot-links{top:3155px;font-size:15px;color:#444;word-spacing:2px}
.copyright{top:3192px;font-size:15px;color:#555}
</style>
</head>
<body>
<div class="page">

  <header class="hero" role="img" aria-label="Harbour city skyline with bridge and opera house at sunset"></header>
  <div class="brand"><span class="brand-dot"></span>BRACKEN LOFT</div>
  <svg class="menu-toggle" width="40" height="26" viewBox="0 0 40 26" aria-label="Menu">
    <rect x="0" y="0" width="40" height="3" fill="#fff"/>
    <rect x="10" y="11" width="30" height="3" fill="#fff"/>
    <rect x="4" y="22" width="36" height="3" fill="#fff"/>
  </svg>
  <h1 class="abs center hero-title">BRACKEN LOFT</h1>
  <p class="abs center hero-sub">We are a software development consultancy</p>
  <a class="btn-quote">GET A QUOTE</a>

  <h2 class="abs center section-title" style="top:707px">THE THREE FACES OF BRACKEN LOFT</h2>
  <p class="abs center section-sub" style="top:766px">We are all about building software better</p>

  <div class="service" style="left:98px">
    <svg width="80" height="70" viewBox="0 0 80 70">
      <path d="M8 6h42a6 6 0 0 1 6 6v20a6 6 0 0 1-6 6H24l-12 10v-10H8a6 6 0 0 1-6-6V12a6 6 0 0 1 6-6z" fill="none" stroke="#ec1f27" stroke-width="5"/>
      <path d="M60 22h10a6 6 0 0 1 6 6v18a6 6 0 0 1-6 6h-2v10l-12-10H40a6 6 0 0 1-6-6v-4" fill="none" stroke="#ec1f27" stroke-width="5"/>
    </svg>
    <h3>CONSULTING</h3>
    <p>Up-skill your team by using our consultants - for either short or long term engagements.</p>
  </div>
  <div class="service" style="left:441px">
    <svg width="84" height="76" viewBox="0 0 84 76">
      <g fill="#ec1f27">
        <circle cx="32" cy="40" r="20"/>
        <g transform="translate(32 40)">
          <rect x="-5" y="-28" width="10" height="12"/><rect x="-5" y="16" width="10" height="12"/>
          <rect x="-28" y="-5" width="12" height="10"/><rect x="16" y="-5" width="12" height="10"/>
          <rect x="-5" y="-28" width="10" height="12" transform="rotate(45)"/><rect x="-5" y="-28" width="10" height="12" transform="rotate(135)"/>
          <rect x="-5" y="-28" width="10" height="12" transform="rotate(225)"/><rect x="-5" y="-28" width="10" height="12" transform="rotate(315)"/>
        </g>
        <circle cx="66" cy="16" r="10"/><circle cx="66" cy="60" r="10"/>
      </g>
      <circle cx="32" cy="40" r="7" fill="#fff"/><circle cx="66" cy="16" r="4" fill="#fff"/><circle cx="66" cy="60" r="4" fill="#fff"/>
    </svg>
    <h3>PROJECTS</h3>
    <p>We can deliver a large project on a fixed price basis at a quality standard you won't believe</p>
  </div>
  <div class="service" style="left:785px">
    <svg width="72" height="72" viewBox="0 0 72 72" aria-label="Completed check">
      <circle cx="36" cy="36" r="31" fill="none" stroke="#ec1f27" stroke-width="5"/>
      <path d="M22 37l10 10 19-21" fill="none" stroke="#ec1f27" stroke-width="5" stroke-linecap="round" stroke-linejoin="round"/>
    </svg>
    <h3>SHEETWISE</h3>
    <p>Our product, Sheetwise, allows you to skip the development cycle and turn an excel spreadsheet directly into either a web service or a web site</p>
  </div>

  <section class="band-grey"></section>
  <div class="wwd-frame"></div>
  <h2 class="wwd-title">WHAT WE DO</h2>
  <div class="wwd-copy">
    <p>Nam libero tempore, cum soluta nobis est eligendi optio cumquehil impedit quo minus id quod maxime placea..</p>
    <p>facere possimus, omnis voluptas assumenda est, omnis dolor repell At vero eos et accusamus et iusto odio dignissimos ducimus quiblan ditiis praesenend oribus aute uibusdam.</p>
  </div>
  <a class="btn-outline">READ MORE</a>
  <div class="video" role="img" aria-label="Video still of a business meeting in an office"></div>
  <svg class="play" width="68" height="68" viewBox="0 0 68 68" aria-label="Play video">
    <circle cx="34" cy="34" r="32" fill="#111" fill-opacity=".85"/>
    <path d="M27 20l22 14-22 14z" fill="#fff"/>
  </svg>

  <h2 class="abs center section-title" style="top:1860px">MEET OUR LEADERSHIP TEAM</h2>
  <p class="abs center team-intro">Between just the partners, we have more than 60 years of software development experience. We combine a solid<br>knowledge of computer science with a practical, pragmatic approach to delivering software.</p>

  <div class="member" style="left:70px">
    <div class="avatar"><span role="img" aria-label="Portrait photo of Grant Mellow"></span></div>
    <h4>Grant Mellow</h4><div class="role">PARTNER</div>
    <p>Grant's one of the best developers on the planet</p>
  </div>
  <div class="member" style="left:448px">
    <div class="avatar"><span role="img" aria-label="Portrait photo of Owen Tulley"></span></div>
    <h4>Owen Tulley</h4><div class="role">PARTNER</div>
    <p>Owen's been running software projects for 20 years</p>
  </div>
  <div class="member" style="left:826px">
    <div class="avatar"><span role="img" aria-label="Portrait photo of Callum Reddin"></span></div>
    <h4>Callum Reddin</h4><div class="role">PARTNER</div>
    <p>Callum codes for fun as much as he does for work</p>
  </div>

  <section class="contact" role="img" aria-label="Red tinted photo of an office workspace"></section>
  <h2 class="abs center contact-title">GET IN TOUCH</h2>
  <div class="field" style="left:259px;top:2637px;width:335px;height:41px">First Name</div>
  <div class="field" style="left:607px;top:2637px;width:334px;height:41px">Last Name</div>
  <div class="field" style="left:259px;top:2691px;width:335px;height:41px">Email Address</div>
  <div class="field" style="left:607px;top:2691px;width:334px;height:41px">Phone Number</div>
  <div class="field" style="left:259px;top:2746px;width:682px;height:80px">Message</div>
  <a class="btn-submit">SUBMIT</a>

  <span class="social" style="left:482px" aria-label="Social link"></span>
  <span class="social" style="left:538px" aria-label="Social link"></span>
  <span class="social" style="left:597px" aria-label="Social link"></span>
  <span class="social" style="left:655px" aria-label="Social link"></span>

  <p class="abs center foot-line" style="top:3115px">
    <svg width="12" height="16" viewBox="0 0 12 16"><path d="M6 0a6 6 0 0 1 6 6c0 4-6 10-6 10S0 10 0 6a6 6 0 0 1 6-6z" fill="#ec1f27"/><circle cx="6" cy="6" r="2.2" fill="#fff"/></svg>
    42 - 44 Harbour Lane, Sydney 2000<span class="sep">|</span>
    <svg width="15" height="15" viewBox="0 0 16 16"><path d="M3 1l3 3-2 2a10 10 0 0 0 6 6l2-2 3 3-2 3C7 16 0 9 0 3z" fill="#ec1f27"/></svg>
    1 800 555 0142<span class="sep">|</span>
    <svg width="17" height="13" viewBox="0 0 17 13"><rect width="17" height="13" rx="1.5" fill="#ec1f27"/><path d="M1 1l7.5 6L16 1" fill="none" stroke="#fff" stroke-width="1.5"/></svg>
    info@brackenloft.com.au
  </p>
  <p class="abs center foot-links">Help<span class="sep" style="margin:0 14px">|</span>FAQ<span class="sep" style="margin:0 14px">|</span>Support<span class="sep" style="margin:0 14px">|</span>Sitemap<span class="sep" style="margin:0 14px">|</span>Terms Of Use<span class="sep" style="margin:0 14px">|</span>Privacy Statement</p>
  <p class="abs center copyright">Bracken Loft © 2018 All rights reserved.</p>

</div>
</body>
</html>
```